Luminar Optics

I wish to make a mailing of a postcard format to pathologists in the UK. Probable number between 500 and 1000.There are 3 elements. 1. A small number of words (about 12) 2. A picture of our product 3. A relevant (tissue section) background. I have knocked up a rough idea of what I want ... BUT ... I'm obviously not a designer. The text looks awful and needs some way of standing out (and being legible) against the background. I can send original images of product and background. Important ... Aspect ratios of images must not be changed.
Look and feel
Each slider illustrates characteristics of the customer's brand and the style your logo design should communicate.

```html
<!DOCTYPE html>
<html lang="en">
<head>
<meta charset="utf-8">
<title>Luminar Optics – Postcard</title>
<link href="https://fonts.googleapis.com/css2?family=Open+Sans:ital,wght@0,600;0,700;1,700;1,800&display=swap" rel="stylesheet">
<style>
  :root {
    --plum: #6b3e6e;
    --plum-deep: #5a2f5d;
    --ink: #1c1a1d;
    --paper: #ffffff;
    --edge: #c9c6cb;
    --tissue-light: #e7b6d4;
    --tissue-mid: #c77fb0;
    --tissue-dark: #8d4f88;
  }
  html, body {
    margin: 0;
    padding: 0;
    width: 1200px;
    height: 572px;
    overflow: hidden;
    background: var(--paper);
    font-family: "Open Sans", Arial, sans-serif;
  }
  .canvas {
    position: relative;
    width: 1200px;
    height: 572px;
  }

  /* ---------- Front of card ---------- */
  .front {
    position: absolute;
    left: 0;
    top: 0;
    width: 442px;
    height: 566px;
    background: var(--paper);
    border-right: 1px solid var(--edge);
    border-bottom: 1px solid var(--edge);
    overflow: hidden;
  }
  .front__tissue {
    position: absolute;
    inset: 0;
  }
  .front__title {
    position: absolute;
    left: 30px;
    top: 24px;
    margin: 0;
    color: var(--plum);
    font-style: italic;
    font-weight: 800;
    font-size: 27px;
    letter-spacing: -0.2px;
  }
  .benefits {
    position: absolute;
    left: 38px;
    top: 74px;
    margin: 0;
    padding: 0;
    list-style: none;
    display: grid;
    grid-template-columns: 180px 180px;
    row-gap: 2px;
    color: var(--ink);
    font-weight: 700;
    font-size: 28px;
  }
  .benefits li::before {
    content: "•";
    margin-right: 12px;
  }
  .product-shot {
    position: absolute;
    left: 108px;
    top: 182px;
    width: 232px;
    height: 158px;
    border-radius: 26px 30px 8px 8px;
    background: linear-gradient(160deg, #fafafa 0%, #e6e6e8 60%, #c9c9cc 100%);
    box-shadow: 0 4px 10px rgba(0,0,0,0.18);
  }
  .front__brand {
    position: absolute;
    left: 0;
    right: 0;
    top: 515px;
    display: flex;
    justify-content: center;
    align-items: center;
    gap: 9px;
  }

  /* ---------- Back of card ---------- */
  .back {
    position: absolute;
    left: 558px;
    top: 64px;
    width: 607px;
    height: 441px;
    background: var(--paper);
    border: 1px solid var(--edge);
    box-shadow: 5px 5px 5px rgba(0,0,0,0.35);
    overflow: hidden;
  }
  .back__tissue {
    position: absolute;
    inset: 0;
  }
  .brand-tab {
    position: absolute;
    left: 78px;
    top: 0;
    width: 178px;
    height: 48px;
    background: var(--paper);
    border-radius: 0 0 16px 16px;
    display: flex;
    justify-content: center;
    align-items: center;
    gap: 8px;
  }
  .brand-mark {
    width: 14px;
    height: 14px;
    background: var(--ink);
    flex: none;
  }
  .brand-name {
    color: var(--ink);
    font-weight: 700;
    font-size: 17px;
  }
  .back__headline {
    position: absolute;
    left: 40px;
    top: 178px;
    width: 250px;
    margin: 0;
    text-align: center;
    color: var(--paper);
    font-style: italic;
    font-weight: 800;
    font-size: 48px;
    line-height: 1.12;
    letter-spacing: -0.5px;
    -webkit-text-stroke: 1.5px var(--ink);
    paint-order: stroke fill;
    text-shadow: 2px 2px 3px rgba(0,0,0,0.7);
  }
  .contact-band {
    position: absolute;
    left: 0;
    top: 321px;
    width: 328px;
    height: 72px;
    background: var(--plum);
    color: var(--paper);
    text-align: center;
    box-sizing: border-box;
    padding-top: 8px;
  }
  .contact-band__phone {
    display: block;
    font-weight: 700;
    font-size: 27px;
    line-height: 1.1;
  }
  .contact-band__web {
    display: block;
    font-style: italic;
    font-weight: 700;
    font-size: 19px;
    line-height: 1.3;
  }
</style>
</head>
<body>
<main class="canvas">

  <section class="front">
    <svg class="front__tissue" width="442" height="566" viewBox="0 0 442 566" role="img" aria-label="Stained tissue section micrograph in pink and purple tones">
      <defs>
        <linearGradient id="tissueFront" x1="0" y1="0" x2="1" y2="1">
          <stop offset="0" stop-color="var(--tissue-mid)"/>
          <stop offset="0.45" stop-color="var(--tissue-light)"/>
          <stop offset="0.75" stop-color="var(--tissue-mid)"/>
          <stop offset="1" stop-color="var(--tissue-dark)"/>
        </linearGradient>
      </defs>
      <path d="M0 212 Q221 300 442 214 L442 530 Q221 500 0 530 Z" fill="url(#tissueFront)"/>
      <path d="M0 226 Q221 314 442 228" fill="none" stroke="#fff" stroke-width="3"/>
    </svg>

    <h1 class="front__title">Whole Slide Scanning is now ...</h1>
    <ul class="benefits">
      <li>Compact</li>
      <li>Simple</li>
      <li>Fast</li>
      <li>Affordable</li>
    </ul>

    <div class="product-shot" role="img" aria-label="Photograph of the compact whole slide scanner"></div>

    <div class="front__brand">
      <span class="brand-mark"></span>
      <span class="brand-name">Luminar Optics</span>
    </div>
  </section>

  <section class="back">
    <svg class="back__tissue" width="607" height="441" viewBox="0 0 607 441" role="img" aria-label="Vertical band of stained tissue section in pink and purple tones">
      <defs>
        <linearGradient id="tissueBack" x1="0" y1="0" x2="0.3" y2="1">
          <stop offset="0" stop-color="var(--tissue-mid)"/>
          <stop offset="0.5" stop-color="var(--tissue-light)"/>
          <stop offset="1" stop-color="var(--tissue-mid)"/>
        </linearGradient>
      </defs>
      <path d="M28 0 L274 0 Q232 220 274 441 L28 441 Q78 220 28 0 Z" fill="url(#tissueBack)"/>
      <path d="M44 0 Q92 220 44 441" fill="none" stroke="#fff" stroke-width="3"/>
      <path d="M258 0 Q216 220 258 441" fill="none" stroke="#fff" stroke-width="3"/>
    </svg>

    <div class="brand-tab">
      <span class="brand-mark"></span>
      <span class="brand-name">Luminar Optics</span>
    </div>

    <h2 class="back__headline">It's worth a look!</h2>

    <div class="contact-band">
      <span class="contact-band__phone">+44 1632 960418</span>
      <span class="contact-band__web">www.luminaroptics.com</span>
    </div>
  </section>

</main>
</body>
</html>
```